Postcard Design

I have prduced a documentary film and I would like to create a post card to help promote and announce the film and how to purchase the film. my web site shold be mentioned BrellcastFilms.com

There is a discription of the current FILM called MARLOW at the above web site .

I think I wil also use MARLOW the movie .com as a registered do mane name

The flip side of the card should promote a conference, that is still being planned, but information can be found at Lumaridge gathering.com the event will be in Heber in 2015 November 5 -6-7, 2015. It will be the 40th anniversary of this historic UFO encounter which my documentary is focused.

Meet Marlow Denby and other UFO experts at this three day conference.

Visit the acutual encounter location in the Sitgraves National Forrest with Marlow Thursday November 5th, 2015. 40 years to the date of his dissapearence. Night watch lead by Cole Pruett and Marlow Denby.
Updates

The second site of the post card promoting the film annoucment should promote the upcoming Marlow Denby 40th Aniversary UFO conference on NOvember 5th 2015 to November 8th. In Heber Arizona. visit: http://www.lumaridgegathering.com for more information. You can pull some information form the site. I have also uploaded graphics for this announcement. I like the first design posted but the wording should be improved to read better... there is wording on the dvd cover to draw from that is better langueged. It was a UFO incident or "encounter" of the third kind, is even a better description. It made international headlines and contiues to to astound UFO researchers, journalist, police, and the media. rather than just a UFO event.

Target Market(s)

This market will be people interested in comming to a UFO conference, or interested in learning about this topic thru film. Can be all walks of people form al different socio economic backgrounds. There are the people hunger for information that has been hidden from them, other experiencers especially like to meet people of a like mind where they can speak freely with out fear of ridicule.

Industry/Entity Type

Movie

Font styles to use
Serif

Colors
faa54b
9d9d9d
fece3f

Requirements
Must have
• Current web sites on one card are wrong,

Movie web site is MarlowDenbythemovie.com

Web site for conference is www.lumaridgegathering.com

Web sites listed, as this shows how to buy the film and how to register for the conference. For the film side of the card it should say for screening inquires contact Rosalind K. Farrow - Brellcast Films.com
Nice to have
• Idealy I'd like to have a promo card that is two sided with out being a mailer. Can this be done?

You can take grphics form the luma ridge gathering web site too if you want for the promo card siade about the conference.

```html
<!DOCTYPE html>
<html lang="en">
<head>
<meta charset="utf-8">
<title>MARLOW – UFO encounter of the third kind</title>
<link rel="stylesheet" href="https://fonts.googleapis.com/css2?family=Gelasio:ital,wght@0,400;0,700;1,700&family=Luckiest+Guy&display=swap">
<style>
  :root {
    --page-bg: #e9e4dc;
    --night-deep: #07090a;
    --night-forest: #1c2a28;
    --night-haze: #2f3a3c;
    --title-yellow: #fece3f;
    --quote-orange: #faa54b;
    --panel-grey: rgba(157, 157, 157, 0.32);
    --detail-grey: #d9d9d9;
    --frame-yellow: #fec95a;
    --text-white: #ffffff;
    --logo-ink: #1a1a1a;
  }
  * { box-sizing: border-box; margin: 0; padding: 0; }
  html, body {
    width: 1200px;
    height: 817px;
    overflow: hidden;
    background: var(--page-bg);
  }
  .postcard {
    position: absolute;
    left: 85px;
    top: 10px;
    width: 1030px;
    height: 796px;
    overflow: hidden;
  }
  .postcard__scene {
    position: absolute;
    inset: 0;
    background:
      radial-gradient(ellipse at 92% 88%, rgba(200, 190, 120, 0.35) 0, rgba(200, 190, 120, 0) 18%),
      radial-gradient(ellipse at 78% 70%, rgba(90, 100, 100, 0.55) 0, rgba(40, 50, 50, 0) 45%),
      radial-gradient(ellipse at 20% 10%, var(--night-forest) 0, rgba(20, 30, 28, 0) 55%),
      linear-gradient(180deg, var(--night-haze) 0%, var(--night-deep) 35%, var(--night-deep) 65%, #1a2218 100%);
  }
  .postcard__title {
    position: absolute;
    top: 26px;
    left: 0;
    width: 100%;
    text-align: center;
    font-family: "Luckiest Guy", "Gelasio", serif;
    font-weight: 400;
    font-size: 56px;
    letter-spacing: 2px;
    color: var(--title-yellow);
  }
  .postcard__subtitle {
    position: absolute;
    top: 92px;
    left: 0;
    width: 100%;
    text-align: center;
    font-family: "Gelasio", serif;
    font-size: 37px;
    color: var(--text-white);
  }
  .postcard__photo {
    position: absolute;
    left: 21px;
    top: 240px;
    width: 454px;
    height: 360px;
    border: 8px solid var(--frame-yellow);
    background: linear-gradient(160deg, #7fa65a 0%, #5c8a3c 35%, #9aa0a2 60%, #3f5a7a 100%);
  }
  .postcard__panel {
    position: absolute;
    left: 536px;
    top: 239px;
    width: 478px;
    height: 360px;
    background: var(--panel-grey);
  }
  .postcard__quote {
    position: absolute;
    left: 553px;
    top: 356px;
    width: 450px;
    font-family: "Gelasio", serif;
    font-size: 27px;
    line-height: 40px;
    color: var(--quote-orange);
    white-space: nowrap;
  }
  .postcard__details {
    position: absolute;
    left: 556px;
    top: 494px;
    width: 440px;
    font-family: "Gelasio", serif;
    font-size: 18px;
    line-height: 26px;
    color: var(--detail-grey);
  }
  .postcard__details strong {
    font-weight: 700;
    color: var(--text-white);
  }
  .postcard__brand {
    position: absolute;
    left: 24px;
    top: 697px;
    width: 293px;
    height: 72px;
    background: var(--text-white);
    display: flex;
    align-items: center;
    justify-content: center;
    font-family: "Gelasio", serif;
    font-size: 26px;
    color: var(--logo-ink);
  }
  .postcard__links {
    position: absolute;
    right: 25px;
    top: 688px;
    text-align: right;
    font-family: "Gelasio", serif;
    font-style: italic;
    font-weight: 700;
    font-size: 30px;
    line-height: 46px;
    color: var(--text-white);
    white-space: nowrap;
  }
</style>
</head>
<body>
  <main class="postcard">
    <div class="postcard__scene" role="img" aria-label="Painted night scene of a dark forest with an old pickup truck, headlight glowing"></div>
    <h1 class="postcard__title">MARLOW</h1>
    <p class="postcard__subtitle">UFO encounter of the third kind</p>
    <div class="postcard__photo" role="img" aria-label="Photo of an interview being filmed in a garden, with camera tripod and umbrella light"></div>
    <div class="postcard__panel"></div>
    <p class="postcard__quote">“ Meet Marlow Denby and other<br>UFO experts at this three day<br>conference. ”</p>
    <p class="postcard__details"><strong>November 5–7, 2015 · Heber, Arizona</strong><br>Screening inquiries: Rosalind K. Farrow<br>Brellcast Films.com</p>
    <div class="postcard__brand">Brellcast Films</div>
    <p class="postcard__links">www.lumaridgegathering.com<br>MarlowDenbythemovie.com</p>
  </main>
</body>
</html>
```